Intranet for company management ERP Style

We need a redesign for our Intranet webpage (Images, CSS), we have all the code and functionality ready and a basic design but it is not good looking. In order to meet our company standards this design has to be fully responsive and elegant, also should display the colors of the company: (#F17808 #EDAA64 #F4B947 #F2A900 #292828 #3D3D3D #062953) usually Dark orange colors are the main ones, though we wouldn't mind to see other options or to implement a pair of skins that we could switch easily on the webpage.
Access to the webpage can be granted

Target Market(s)

this webpage is for internal use of the company but could also be sold to external customers in the future, our market is cryptocurrency and BPO

Industry/Entity Type

BPO, Cryptocurrency

Coding

Coded - Design and coding required

Number of Pages Required

1 page

Font styles to use
Other font styles liked:
• Headings: Montserrat Extra Bold, Sub headings: Montserrat, Text: Object Sans

Colors
F0912C
F2A743
F7CA91
FBE8D2
FDF5EE

Requirements
Nice to have
• elegant icons designs and menus

```html
<!DOCTYPE html>
<html lang="en">
<head>
<meta charset="utf-8">
<title>Intranet for Company management ERP Style – Dashboard</title>
<link rel="stylesheet" href="https://fonts.googleapis.com/css2?family=Montserrat:wght@400;500;600;700;800&display=swap">
<style>
:root{
  --orange-dark:#F17808;
  --orange:#F0912C;
  --orange-mid:#F2A743;
  --orange-light:#F4B947;
  --peach:#F7CA91;
  --cream:#FBE8D2;
  --bg:#FDF5EE;
  --ink:#292828;
  --ink-soft:#3D3D3D;
  --grey:#6b6b6b;
  --line:#ececec;
}
*{box-sizing:border-box;margin:0;padding:0}
html,body{width:1161px;height:1200px;overflow:hidden}
body{font-family:'Montserrat',sans-serif;background:var(--bg);color:var(--ink);position:relative}

/* Sidebar */
.sidebar{position:absolute;left:0;top:0;width:189px;height:1200px;background:var(--orange)}
.brand{height:108px;background:var(--orange-mid);display:flex;align-items:center;padding-left:14px;gap:10px;color:#fff}
.brand-dot{width:34px;height:34px;border-radius:50%;background:#fff;opacity:.9;flex:none}
.brand-text{line-height:1.1;color:var(--ink)}
.brand-text small{display:block;font-size:9px;font-weight:500}
.brand-text span{display:block;font-size:13px;font-weight:500}
.brand-text strong{display:block;font-size:17px;font-weight:700}
.menu{list-style:none;padding-top:28px}
.menu li{display:flex;align-items:center;gap:13px;height:46px;padding-left:22px;color:#fff;font-size:13px;font-weight:500}
.menu svg{width:20px;height:20px;stroke:#fff;fill:none;stroke-width:1.4}

/* Topbar */
.topbar{position:absolute;left:189px;top:0;width:972px;height:43px;background:#fff;display:flex;align-items:center;padding:0 14px 0 15px}
.topbar .left,.topbar .right{display:flex;gap:14px;align-items:center}
.topbar .right{margin-left:auto;gap:16px}
.topbar svg{width:19px;height:19px;stroke:var(--ink);fill:none;stroke-width:1.8}
.badge{position:relative}
.badge::after{content:"";position:absolute;right:-3px;top:-2px;width:6px;height:6px;border-radius:50%;background:var(--orange-light)}
.avatar{width:31px;height:31px;border-radius:50%;background:var(--cream);border:2px solid #fff;box-shadow:0 0 0 1px var(--line)}

/* Page head */
.page-title{position:absolute;left:211px;top:59px;font-size:16px;font-weight:600;color:var(--orange-dark)}
.crumbs{position:absolute;left:211px;top:81px;font-size:11px;color:var(--ink-soft)}

.card{position:absolute;background:#fff;box-shadow:0 1px 4px rgba(0,0,0,.05)}

/* Banner */
.banner{left:212px;top:110px;width:608px;height:286px;padding:4px}
.banner-art{width:100%;height:100%;background:linear-gradient(100deg,#E5262A 0%,#EE3B2B 40%,#F4B62A 48%,#F0C52E 70%,#EDA82A 100%)}

/* Gamification */
.gamify{position:absolute;left:844px;top:110px;width:294px;height:286px;background:var(--orange)}
.gamify h2{height:53px;background:var(--orange-dark);color:#fff;font-size:17px;font-weight:700;padding:16px 15px 0}
.gamify ul{list-style:none;padding:0 15px}
.gamify li{height:51px;display:flex;align-items:center;gap:9px;color:#fff;font-size:14px;font-weight:500;border-bottom:1px solid rgba(255,255,255,.25)}
.gamify li:last-child{border:0}
.gamify svg{width:26px;height:26px;stroke:#fff;fill:none;stroke-width:1.3}
.gamify .tag{margin-left:auto;border:1px solid rgba(255,255,255,.6);border-radius:3px;font-size:11px;padding:3px 10px;color:var(--ink-soft)}

/* Stats */
.stat{top:420px;width:293px;height:110px;padding:16px 15px}
.stat h3{font-size:13px;font-weight:500}
.stat p{font-size:12px;color:var(--grey);margin-top:25px}
.stat strong{display:block;font-size:17px;font-weight:600;margin-top:5px}
.stat .score{position:absolute;right:15px;top:20px;width:77px;height:70px;border-radius:6px;color:#fff;font-size:24px;font-weight:700;display:flex;align-items:center;justify-content:center}

/* Calendar */
.calendar{left:212px;top:553px;width:926px;height:565px}
.cal-title{position:absolute;left:0;width:100%;top:15px;text-align:center;font-size:16px;font-weight:500;color:var(--orange-dark)}
.cal-tools{position:absolute;right:22px;top:13px;display:flex;gap:4px}
.cal-tools span{border:1px solid #ddd;font-size:9px;padding:4px 5px;border-radius:2px;color:var(--ink-soft);background:#fff}
.cal-tools .on{background:var(--orange-dark);border-color:var(--orange-dark);color:#fff}
.cal-grid{position:absolute;left:21px;top:45px;width:882px}
.cal-head,.week{display:grid;grid-template-columns:repeat(7,1fr)}
.cal-head div{height:26px;background:var(--orange-dark);color:#fff;font-size:11px;font-weight:600;text-align:center;line-height:26px;border-right:1px solid rgba(255,255,255,.6)}
.week{position:relative;height:94px;border-bottom:1px solid var(--line)}
.week:last-child{height:89px}
.week>.day{border-left:1px solid var(--line);text-align:right;padding:8px 9px;font-size:14px;color:#555;position:relative}
.week>.day:last-of-type{border-right:1px solid var(--line)}
.week .muted{color:#ddd}
.event{display:block;position:absolute;text-align:left;font-size:8.5px;line-height:1.55;padding:7px 11px;border-left:2px solid}
.vacation{left:10px;top:30px;width:862px;height:52px;background:#E1F2FC;border-color:#2E8FD0;color:#1f78b4}
.meeting{left:10px;top:32px;width:104px;height:51px;background:#FBF3D6;border-color:#9BBF3A;color:#7a9a1e;padding-top:11px}
.birthday{left:12px;top:32px;width:104px;height:51px;background:#FBF3D6;border-color:#F2A900;color:#D68A00;padding-top:6px}
.series{left:9px;top:31px;width:104px;height:51px;background:#f2f2f2;border-color:#555;color:#555}

/* Footer */
.footer{position:absolute;left:189px;top:1158px;width:972px;height:42px;background:var(--ink-soft);color:#cfcfcf;font-size:13px;text-align:center;line-height:42px}
</style>
</head>
<body>

<aside class="sidebar">
  <div class="brand">
    <div class="brand-dot"></div>
    <div class="brand-text"><small>Intranet for Company</small><span>management</span><strong>ERP Style</strong></div>
  </div>
  <ul class="menu">
    <li><svg viewBox="0 0 24 24"><path d="M3 16a9 9 0 1 1 18 0"/><path d="M12 16l4-5"/><circle cx="12" cy="16" r="1"/></svg>Home</li>
    <li><svg viewBox="0 0 24 24"><circle cx="8" cy="12" r="3"/><path d="M2 21c0-3 3-5 6-5s6 2 6 5"/><rect x="12" y="3" width="9" height="6" rx="1"/></svg>Requests</li>
    <li><svg viewBox="0 0 24 24"><rect x="4" y="3" width="16" height="18" rx="1"/><path d="M7 16l3-4 3 2 4-5"/></svg>Reports</li>
    <li><svg viewBox="0 0 24 24"><circle cx="12" cy="8" r="4"/><path d="M5 21c0-4 3-7 7-7s7 3 7 7"/><path d="M7 8a5 5 0 0 1 10 0"/></svg>Helpdesk</li>
    <li><svg viewBox="0 0 24 24"><circle cx="14" cy="7" r="4"/><path d="M2 17h4l4 2 8-3"/><path d="M2 14h5l5 1"/></svg>Payroll</li>
    <li><svg viewBox="0 0 24 24"><rect x="4" y="12" width="16" height="9"/><rect x="7" y="3" width="10" height="10"/><path d="M9 7h6M9 10h6"/></svg>Suggestion Box</li>
    <li><svg viewBox="0 0 24 24"><circle cx="12" cy="7" r="4"/><path d="M4 21c0-4 4-7 8-7s8 3 8 7z"/></svg>Administrator</li>
  </ul>
</aside>

<header class="topbar">
  <div class="left">
    <svg viewBox="0 0 24 24"><path d="M3 6h18M3 12h18M3 18h18"/></svg>
    <svg viewBox="0 0 24 24"><circle cx="10" cy="10" r="7"/><path d="M15 15l6 6"/></svg>
    <svg viewBox="0 0 24 24"><rect x="3" y="3" width="7" height="7"/><rect x="14" y="3" width="7" height="7"/><rect x="3" y="14" width="7" height="7"/><rect x="14" y="14" width="7" height="7"/></svg>
  </div>
  <div class="right">
    <span class="badge"><svg viewBox="0 0 24 24"><path d="M3 4h18v12H9l-5 4v-4H3z"/><path d="M7 8h10M7 12h6"/></svg></span>
    <span class="badge"><svg viewBox="0 0 24 24"><rect x="2" y="5" width="20" height="14"/><path d="M2 5l10 8 10-8"/></svg></span>
    <span class="avatar"></span>
  </div>
</header>

<h1 class="page-title">Dashboard</h1>
<div class="crumbs">Home &gt; dashboard</div>

<section class="card banner">
  <div class="banner-art" role="img" aria-label="Promotional sale banner with red and yellow geometric shapes"></div>
</section>

<section class="gamify">
  <h2>Gamification</h2>
  <ul>
    <li><svg viewBox="0 0 24 24"><circle cx="12" cy="9" r="7"/><path d="M12 5l1.3 2.6 2.9.4-2.1 2 .5 2.9-2.6-1.4-2.6 1.4.5-2.9-2.1-2 2.9-.4z"/><path d="M7 14l-3 7 3-1 2 2 2-6M17 14l3 7-3-1-2 2-2-6"/></svg>Lorem Ipsum<span class="tag">demo</span></li>
    <li><svg viewBox="0 0 24 24"><circle cx="12" cy="9" r="7"/><path d="M12 5l1.3 2.6 2.9.4-2.1 2 .5 2.9-2.6-1.4-2.6 1.4.5-2.9-2.1-2 2.9-.4z"/><path d="M7 14l-3 7 3-1 2 2 2-6M17 14l3 7-3-1-2 2-2-6"/></svg>Lorem Ipsum<span class="tag">demo</span></li>
    <li><svg viewBox="0 0 24 24"><circle cx="12" cy="9" r="7"/><path d="M12 5l1.3 2.6 2.9.4-2.1 2 .5 2.9-2.6-1.4-2.6 1.4.5-2.9-2.1-2 2.9-.4z"/><path d="M7 14l-3 7 3-1 2 2 2-6M17 14l3 7-3-1-2 2-2-6"/></svg>Lorem Ipsum<span class="tag">demo</span></li>
    <li><svg viewBox="0 0 24 24"><circle cx="12" cy="9" r="7"/><path d="M12 5l1.3 2.6 2.9.4-2.1 2 .5 2.9-2.6-1.4-2.6 1.4.5-2.9-2.1-2 2.9-.4z"/><path d="M7 14l-3 7 3-1 2 2 2-6M17 14l3 7-3-1-2 2-2-6"/></svg>Lorem Ipsum<span class="tag">demo</span></li>
  </ul>
</section>

<section class="card stat" style="left:212px"><h3>CSAT</h3><p>Lorem Ipsum</p><strong>72,568,452</strong><div class="score" style="background:var(--orange-light)">3.2</div></section>
<section class="card stat" style="left:529px"><h3>CSAT</h3><p>Lorem Ipsum</p><strong>72,568,452</strong><div class="score" style="background:var(--orange)">3.2</div></section>
<section class="card stat" style="left:845px"><h3>CSAT</h3><p>Lorem Ipsum</p><strong>72,568,452</strong><div class="score" style="background:var(--orange-dark)">3.2</div></section>

<section class="card calendar">
  <div class="cal-title">January 2022</div>
  <div class="cal-tools"><span>&lsaquo; &nbsp;Today&nbsp; &rsaquo;</span><span>Day</span><span>Week</span><span class="on">Month</span><span>Year</span><span>List</span><span>Planner</span></div>
  <div class="cal-grid">
    <div class="cal-head"><div>Monday</div><div>Tuesday</div><div>Wednesday</div><div>Thursday</div><div>Friday</div><div>Saturday</div><div>Sunday</div></div>
    <div class="week"><div class="day muted">27</div><div class="day muted">28</div><div class="day muted">29</div><div class="day muted">30</div><div class="day muted">31</div><div class="day">1</div><div class="day">2</div></div>
    <div class="week"><div class="day">3</div><div class="day">4</div><div class="day">5</div><div class="day">6</div><div class="day">7</div><div class="day">8</div><div class="day">9</div>
      <span class="event vacation">Vacation<br>Start: 01/17/2022<br>End: 01/17/2022</span></div>
    <div class="week"><div class="day">10<span class="event meeting">Team Meeting<br>01:30pm</span></div><div class="day">11</div><div class="day">12</div><div class="day">13</div><div class="day">14<span class="event birthday">Birthday<br>Start: 01/18/2022<br>End: 01/18/2022</span></div><div class="day">15</div><div class="day">16</div></div>
    <div class="week"><div class="day">17<span class="event series">Series Event<br>Start: 01/17/2022<br>End: 01/17/2022</span></div><div class="day">18<span class="event series">Series Event<br>Start: 01/17/2022<br>End: 01/17/2022</span></div><div class="day">19<span class="event series">Series Event<br>Start: 01/17/2022<br>End: 01/17/2022</span></div><div class="day">20</div><div class="day">21</div><div class="day">22</div><div class="day">23</div></div>
    <div class="week"><div class="day">24</div><div class="day">25</div><div class="day">26</div><div class="day">27</div><div class="day">28</div><div class="day">29</div><div class="day">30</div></div>
  </div>
</section>

<footer class="footer">Copyright © 2022 Intranet for Company Management ERP Style. All Rights Reserved</footer>
</body>
</html>
```